Create a business Card for a Women Owned Business Body Positive Company. The winner we hope to work with on other projects coming up for grand opening for flyers, postcards, email marketing, facebook page, stationary, labels, tshirt design....
We would like if possible in the background of the card a infinity symbol or crown if it fits into the design if not it's ok. But I am open to all suggestions we had alot problems with the our new logo being created this time sad to say :(

Our colors are Royal Purple, Grey, Black Thank you in advance for your talent, you hard work and your submissions!
Delia and Harriet :)

my Logo is lantern meadow boutique which is purple and has a heart and infinity sign in it and my colors are purple silver and black only of another card i had done nothing else. My logo is LANTERN MEADOW BOUTIQUE LOGO

Industry/Entity Type

Retail

Contact Information for Business Card

website: www.lantrnmeadowboutiques.example email: sales@lanternmeadowboutique.example
Delia Rookwell & Harriet Quinlan Owners

Font styles to use
Script

Colors
b768aa

Requirements
Must have
• COLORS ARE PURPLE BLACK AND GREY
Nice to have
• INFINITY SIGNING IN THE BACKGROUND

```html
<!DOCTYPE html>
<html lang="en">
<head>
<meta charset="utf-8">
<title>Lantern Meadow Boutique – Business Card</title>
<link href="https://fonts.googleapis.com/css2?family=Pinyon+Script&family=Quattrocento+Sans:wght@400&display=swap" rel="stylesheet">
<style>
  :root {
    --page-bg: #e7e3df;
    --purple-deep: #5e2777;
    --purple-mid: #7b3a93;
    --purple-light: #8e4fa3;
    --silver-light: #f1f1f4;
    --silver-mid: #d6d6dc;
    --band-grey: #b9b5b9;
    --text-light: #f3e6ef;
    --brand-purple: #5a2a70;
  }
  * { margin: 0; padding: 0; box-sizing: border-box; }
  html, body {
    width: 1200px;
    height: 1054px;
    overflow: hidden;
    background: var(--page-bg);
  }
  .card {
    position: absolute;
    left: 100px;
    top: 224px;
    width: 1000px;
    height: 606px;
    border-radius: 6px;
    overflow: hidden;
    box-shadow: 0 10px 30px rgba(0,0,0,0.18);
    background: linear-gradient(160deg, var(--silver-light), var(--silver-mid));
  }
  .card-shapes {
    position: absolute;
    inset: 0;
  }
  .owners-names {
    position: absolute;
    left: 46px;
    top: 68px;
    font-family: "Pinyon Script", cursive;
    font-size: 40px;
    color: var(--text-light);
    white-space: nowrap;
  }
  .owners-role {
    position: absolute;
    left: 48px;
    top: 142px;
    font-family: "Quattrocento Sans", sans-serif;
    font-size: 22px;
    color: var(--text-light);
  }
  .contact-list {
    position: absolute;
    left: 46px;
    top: 455px;
    list-style: none;
    font-family: "Quattrocento Sans", sans-serif;
    font-size: 24px;
    color: var(--text-light);
  }
  .contact-list li {
    display: flex;
    align-items: center;
    gap: 16px;
    height: 34px;
  }
  .contact-icon { width: 18px; height: 18px; flex: none; }
  .brand-name {
    position: absolute;
    left: 832px;
    top: 303px;
    transform: translate(-50%, -50%) rotate(-90deg);
    font-family: "Quattrocento Sans", sans-serif;
    font-size: 30px;
    letter-spacing: 3px;
    color: var(--brand-purple);
    white-space: nowrap;
  }
</style>
</head>
<body>
  <div class="card">
    <svg class="card-shapes" width="1000" height="606" viewBox="0 0 1000 606" aria-hidden="true">
      <defs>
        <linearGradient id="purpleFill" x1="0" y1="0" x2="1" y2="1">
          <stop offset="0" stop-color="var(--purple-deep)"/>
          <stop offset="0.55" stop-color="var(--purple-mid)"/>
          <stop offset="1" stop-color="var(--purple-light)"/>
        </linearGradient>
      </defs>
      <path class="edge-band" d="M0 0 H700 Q615 300 715 606 H0 Z" fill="var(--band-grey)"/>
      <path class="purple-panel" d="M0 0 H678 Q592 300 692 606 H0 Z" fill="url(#purpleFill)"/>
    </svg>

    <div class="owners-names">Delia Rookwell &amp; Harriet Quinlan</div>
    <div class="owners-role">owners</div>

    <ul class="contact-list">
      <li>
        <svg class="contact-icon" viewBox="0 0 18 18" aria-hidden="true">
          <rect x="1" y="4" width="16" height="11" fill="var(--text-light)"/>
          <path d="M1 4 L9 10 L17 4" fill="none" stroke="var(--purple-mid)" stroke-width="1.4"/>
        </svg>
        <span>sales@lanternmeadowboutique.example</span>
      </li>
      <li>
        <svg class="contact-icon" viewBox="0 0 18 18" aria-hidden="true">
          <circle cx="9" cy="9" r="7.5" fill="none" stroke="var(--text-light)" stroke-width="1.4"/>
          <ellipse cx="9" cy="9" rx="3.2" ry="7.5" fill="none" stroke="var(--text-light)" stroke-width="1.2"/>
          <line x1="1.5" y1="9" x2="16.5" y2="9" stroke="var(--text-light)" stroke-width="1.2"/>
        </svg>
        <span>www.lantrnmeadowboutiques.example</span>
      </li>
    </ul>

    <div class="brand-name">LANTERN MEADOW BOUTIQUE</div>
  </div>
</body>
</html>
```